Website Refresh

Current Website is CourtFray.net - would like to refresh it up along with adding a few features to it. We have promotional videos that are currently on our Friendboard page that we would like to have on our website . We also need a page of information that the users can interactive with in making choices for themselves. For instance finding their name on the list and picking one of three options for a time.

Target Market(s)

Tennis Players - Male and Female Ages 30-80

Coding

Coded - Design and coding required

Number of Pages Required

5+ page

Requirements
Must have
• Same content, with new functionality for users to make choices. Most match logo and icon

```html
<!DOCTYPE html>
<html lang="en">
<head>
<meta charset="utf-8">
<title>Court Fray – Competitive Tennis Tournaments for Adults</title>
<link href="https://fonts.googleapis.com/css2?family=Raleway:wght@600;700;800&family=Open+Sans:wght@400;600&display=swap" rel="stylesheet">
<style>
:root{
  --green:#8cb02a;
  --green-dark:#5f8a1f;
  --green-deep:#3f6a17;
  --charcoal:#3b3b3d;
  --ink:#1c1c1c;
  --text:#4a4a4a;
  --white:#ffffff;
  --footer:#efefef;
  --copy-bar:#e6e6e6;
}
*{box-sizing:border-box;margin:0;padding:0}
html,body{width:1200px;height:3346px;overflow:hidden}
body{position:relative;background:var(--white);font-family:"Open Sans",Arial,sans-serif;color:var(--text)}
.section{position:absolute;left:0;width:1200px}
.heading{font-family:"Raleway",Arial,sans-serif;font-weight:800;color:var(--ink);text-transform:uppercase}
.btn{display:inline-block;background:var(--green);color:var(--white);font-family:"Raleway",Arial,sans-serif;font-weight:700;font-size:17px;border-radius:30px;text-transform:uppercase;text-align:center}
.wordmark{font-family:"Raleway",Arial,sans-serif;font-weight:700;display:flex;align-items:center;gap:10px}
.wordmark .dot{width:22px;height:22px;border-radius:50%;background:var(--green)}

/* Hero */
.hero{top:0;height:720px;overflow:hidden}
.hero-photo{position:absolute;inset:0;background:linear-gradient(160deg,#6d6a62 0%,#8a4a3a 35%,#a5563e 55%,#5d7a3c 80%,#3f5c2a 100%)}
.hero-shade{position:absolute;inset:0;background:rgba(0,0,0,.25)}
.hero .wordmark{position:absolute;left:160px;top:58px;color:var(--white);font-size:38px}
.nav{position:absolute;left:417px;top:68px;display:flex;gap:24px;font-family:"Raleway",Arial,sans-serif;font-weight:600;font-size:13px;color:var(--white);text-transform:uppercase}
.hero-title{position:absolute;left:0;width:1200px;top:268px;text-align:center;color:var(--white);font-family:"Raleway",Arial,sans-serif;font-weight:800;text-transform:uppercase}
.hero-title .l1{font-size:43px;line-height:52px}
.hero-title .l2{font-size:36px;line-height:46px}
.hero .btn{position:absolute;left:509px;top:382px;width:182px;height:58px;line-height:58px}
.arrow-btn{position:absolute;width:54px;height:54px;border-radius:50%;background:rgba(255,255,255,.55)}
.hero-edge{position:absolute;left:0;top:0}

/* About */
.about{top:720px;height:440px}
.about-photo{position:absolute;left:115px;top:88px;width:452px;height:230px;background:linear-gradient(120deg,#1f3a44,#4f6f7a 50%,#1b3038)}
.about .heading{position:absolute;left:605px;top:68px;font-size:32px}
.about-copy{position:absolute;left:605px;top:128px;width:440px;font-size:14.5px;line-height:23px}
.about-copy p+p{margin-top:12px}
.about .btn{position:absolute;left:598px;top:298px;width:162px;height:52px;line-height:52px;font-size:15px}

/* Provides */
.provides{top:1160px;height:780px;background:linear-gradient(180deg,var(--green-dark),var(--green) 45%,var(--green-deep))}
.provides-roof{position:absolute;left:0;top:0}
.badge{position:absolute;left:574px;width:52px;height:52px;border-radius:50%;background:var(--green);border:5px solid var(--white)}
.provides .heading{position:absolute;left:0;width:1200px;top:76px;text-align:center;color:var(--white);font-size:30px}
.provides-player{position:absolute;left:680px;top:120px;width:400px;height:660px;background:linear-gradient(180deg,#7a5a45,#1f5fa8 40%,#163e7a)}
.feature{position:absolute;left:180px;width:430px;padding-left:86px;color:var(--white);list-style:none}
.feature-icon{position:absolute;left:0;top:-4px;width:68px;height:68px;border-radius:50%;border:2px solid var(--white)}
.feature h3{font-family:"Raleway",Arial,sans-serif;font-weight:800;font-size:17px;line-height:23px;text-transform:uppercase}
.feature p{font-size:14px;line-height:19px;margin-top:4px}

/* Videos */
.videos{top:1940px;height:530px;background:linear-gradient(180deg,var(--white) 55%,#e9e9e9)}
.videos .heading{position:absolute;left:0;width:1200px;top:80px;text-align:center;font-size:30px}
.video{position:absolute;top:152px;width:427px;height:265px}
.video-one{left:160px;background:linear-gradient(180deg,#6f8c86,#4e6b63 60%,#6c7866)}
.video-two{left:609px;background:linear-gradient(180deg,#9ea6a6,#4d6a49 55%,#3c5a7a)}
.play{position:absolute;left:180px;top:100px;width:66px;height:66px;border-radius:50%;background:var(--white)}
.carousel-arrow{position:absolute;top:265px}

/* Testimonials */
.testimonials{top:2410px;height:512px}
.testimonials-roof{position:absolute;left:0;top:0}
.testimonials .heading{position:absolute;left:0;width:1200px;top:130px;text-align:center;color:var(--white);font-size:32px}
.portrait{position:absolute;left:248px;top:213px;width:172px;height:172px;border-radius:50%;background:radial-gradient(circle at 50% 40%,#8a8a80,#2f4a2e)}
.quote{position:absolute;left:462px;top:215px;width:530px;font-size:17.5px;line-height:28px;color:#cfcfcf}
.quote-mark{position:absolute;font-family:Georgia,serif;font-size:70px;color:#bdbdbd;line-height:1}
.quote-name{position:absolute;left:462px;top:370px;font-family:"Raleway",Arial,sans-serif;font-weight:700;font-size:17px;color:var(--white);text-transform:uppercase}
.dots{position:absolute;left:567px;top:460px;display:flex;gap:8px}
.dots span{width:14px;height:14px;border-radius:50%;border:2px solid var(--white)}
.dots span.on{background:var(--white)}

/* Footer */
.footer{top:2922px;height:348px;background:var(--footer)}
.footer .wordmark{position:absolute;left:172px;top:140px;font-size:38px;color:var(--ink)}
.footer-col{position:absolute;top:102px}
.footer-col h4{font-family:"Raleway",Arial,sans-serif;font-weight:800;font-size:15px;color:var(--ink);text-transform:uppercase;margin-bottom:12px}
.footer-col ul{list-style:none;font-size:14px;color:var(--text)}
.contact li{display:flex;align-items:center;gap:12px;height:34px;font-size:15px}
.links li{height:27px}
.social li{display:flex;align-items:center;gap:12px;height:34px}
.social .round{width:24px;height:24px;border-radius:50%;background:#2d5a8a}
.copyright{top:3270px;height:76px;background:var(--copy-bar);border-top:1px solid #d5d5d5;text-align:center;font-size:14px;line-height:76px;color:var(--text)}
</style>
</head>
<body>

<header class="section hero">
  <div class="hero-photo" role="img" aria-label="Photo of a woman returning a tennis ball on a clay court"></div>
  <div class="hero-shade"></div>
  <div class="wordmark"><span>CourtFray</span><span class="dot"></span></div>
  <nav class="nav"><span>About Us</span><span>Tournament</span><span>Testimonial</span><span>Request Fray Hall of Frame</span><span>Contact</span></nav>
  <h1 class="hero-title"><span class="l1">Offering Competitive Tennis</span><br><span class="l2">Tournaments for Adults</span></h1>
  <span class="btn">Read More</span>
  <span class="arrow-btn" style="left:96px;top:347px"><svg width="54" height="54"><path d="M31 17 L21 27 L31 37" fill="none" stroke="#222" stroke-width="3"/></svg></span>
  <span class="arrow-btn" style="left:1047px;top:347px"><svg width="54" height="54"><path d="M23 17 L33 27 L23 37" fill="none" stroke="#222" stroke-width="3"/></svg></span>
  <svg class="hero-edge" width="1200" height="720" viewBox="0 0 1200 720">
    <polygon points="0,578 600,702 1200,578 1200,606 600,726 0,606" fill="var(--green)"/>
    <polygon points="0,606 600,726 1200,606 1200,720 0,720" fill="#fff"/>
  </svg>
</header>

<section class="section about">
  <div class="about-photo" role="img" aria-label="Photo of a tennis player striking a ball"></div>
  <h2 class="heading">About Us</h2>
  <div class="about-copy">
    <p>Court Fray, was created in 2009 as a company designed to organize and run special tennis events for adults.</p>
    <p>The company's goal is to coordinate high quality competition and well organized events, while always trying to exceed expectations. Tennis being a sport of ultimate class, it deserves to be treated as such. Court Fray will bring that class</p>
  </div>
  <span class="btn">Read More</span>
</section>

<section class="section provides">
  <div class="provides-player" role="img" aria-label="Photo of a male tennis player in a blue shirt preparing a forehand"></div>
  <svg class="provides-roof" width="1200" height="120" viewBox="0 0 1200 120">
    <polygon points="0,0 1200,0 1200,84 600,0 0,84" fill="#fff"/>
    <polygon points="0,84 600,0 1200,84 1200,100 600,16 0,100" fill="var(--charcoal)"/>
  </svg>
  <span class="badge" style="top:-26px"></span>
  <h2 class="heading">Court Fray Provides</h2>
  <ul>
    <li class="feature" style="top:178px"><span class="feature-icon"></span><h3>Competition for All Levels</h3><p>All levels from 2.5-5.0 are welcomed and do participate, which creates the perfect environment for those interested</p></li>
    <li class="feature" style="top:310px"><span class="feature-icon"></span><h3>Exclusive Resorts and<br>Destinations</h3><p>Court Fray gets you great rates at amazing resorts and destinations that you probably</p></li>
    <li class="feature" style="top:461px"><span class="feature-icon"></span><h3>One-to-One Communication<br>and Highly Organized</h3><p>Court Fray gets you great rates at amazing resorts and destinations that you probably</p></li>
    <li class="feature" style="top:611px"><span class="feature-icon"></span><h3>Excitement and Fun</h3><p>At Court Fray events the fun and excitement are never ending win or lose.</p></li>
  </ul>
</section>

<section class="section videos">
  <h2 class="heading">Our Videos</h2>
  <svg class="carousel-arrow" style="left:112px" width="30" height="40"><path d="M22 4 L8 20 L22 36" fill="none" stroke="#555" stroke-width="4"/></svg>
  <div class="video video-one" role="img" aria-label="Promotional video still of a beach at sunset"><span class="play"><svg width="66" height="66"><polygon points="26,19 48,33 26,47" fill="#111"/></svg></span></div>
  <div class="video video-two" role="img" aria-label="Promotional video still of players on an outdoor tennis court"><span class="play"><svg width="66" height="66"><polygon points="26,19 48,33 26,47" fill="#111"/></svg></span></div>
  <svg class="carousel-arrow" style="left:1048px" width="30" height="40"><path d="M8 4 L22 20 L8 36" fill="none" stroke="#555" stroke-width="4"/></svg>
</section>

<section class="section testimonials">
  <svg class="testimonials-roof" width="1200" height="512" viewBox="0 0 1200 512">
    <polygon points="0,100 600,24 1200,100 1200,512 0,512" fill="var(--charcoal)"/>
    <polygon points="0,94 600,18 1200,94 1200,112 600,36 0,112" fill="var(--green)"/>
  </svg>
  <span class="badge" style="top:-2px"></span>
  <h2 class="heading">Testimonials</h2>
  <div class="portrait" role="img" aria-label="Portrait photo of the reviewer wearing a cap"></div>
  <span class="quote-mark" style="left:432px;top:200px">“</span>
  <p class="quote">Although I don't play in many tournaments throughout the year, I find the Court Fray event that Marlow and Tessa put on to be excellent. Between being extremely well organized, combined with a strong pool of competition it makes it one I will be keeping on the calendar in the future...</p>
  <span class="quote-mark" style="left:862px;top:322px">”</span>
  <p class="quote-name">Helen Brook</p>
  <div class="dots"><span></span><span class="on"></span><span></span></div>
</section>

<footer class="section footer">
  <div class="wordmark"><span>CourtFray</span><span class="dot"></span></div>
  <div class="footer-col contact" style="left:420px">
    <h4>Contact Us</h4>
    <ul>
      <li><svg width="16" height="18"><path d="M8 17 C3 11 2 9 2 6.5 A6 6 0 0 1 14 6.5 C14 9 13 11 8 17Z" fill="none" stroke="#333" stroke-width="1.6"/><circle cx="8" cy="6.5" r="2" fill="#333"/></svg>Riverton, Ohio</li>
      <li><svg width="16" height="18"><path d="M3 2 L6 2 L7.5 6 L5.5 7.5 C6.5 10 8 11.5 10.5 12.5 L12 10.5 L16 12 L16 15 C9 16 2 9 3 2Z" fill="none" stroke="#333" stroke-width="1.5"/></svg>555-014-2207</li>
      <li><svg width="16" height="18"><rect x="1" y="4" width="14" height="10" fill="none" stroke="#333" stroke-width="1.5"/><path d="M1 4 L8 10 L15 4" fill="none" stroke="#333" stroke-width="1.5"/></svg>info@courtfray.net</li>
    </ul>
  </div>
  <div class="footer-col links" style="left:690px">
    <h4>Company</h4>
    <ul><li>Home</li><li>About us</li><li>Testimonials</li><li>Tournaments</li><li>Contact</li></ul>
  </div>
  <div class="footer-col social" style="left:879px">
    <h4>Get Connected</h4>
    <ul><li><span class="round"></span>Chirpline</li><li><span class="round"></span>Friendboard</li><li><span class="round"></span>ProCircle</li><li><span class="round"></span>Snapgrid</li></ul>
  </div>
</footer>

<div class="section copyright">Copyright © 2019 All right reserved</div>

</body>
</html>
```